Business Brochure for Mobile Fleet Mechanic Company

Make a brochure for an mobile mechanic company that is a Bi-fold 8.5"Wx11"H. A Bi-fold would have the outside and inside design so it is a total of 4 pages at 8.5"x11". The print is 2-sides 17"Wx11"H that folds down to 8.5"Wx11"H.
Should have photo of mechanic working. Blue in logo is Pantone 284C. Will provide text to be added to approved design.

Contact Information for Business Card

2-sided card using the same design elements and colors as the brochure.

```html
<!DOCTYPE html>
<html lang="en">
<head>
<meta charset="utf-8">
<title>RigCare Brochure</title>
<link href="https://fonts.googleapis.com/css2?family=Montserrat:wght@500;600;700;800&family=Open+Sans:wght@400;600;700&family=Oswald:wght@500&display=swap" rel="stylesheet">
<style>
:root{
  --blue:#4a94dc;
  --blue-light:#6cace4;
  --ink:#1f2124;
  --dark:#2a2c30;
  --paper:#efefef;
  --stage:#dcdcdc;
  --text:#3a3a3a;
  --muted:#5a5a5a;
}
*{margin:0;padding:0;box-sizing:border-box}
html,body{width:903px;height:1200px;overflow:hidden;background:var(--stage);font-family:"Open Sans",sans-serif;color:var(--text)}
.canvas{position:relative;width:903px;height:1200px}
.brand-top{position:absolute;top:60px;left:0;width:903px;text-align:center;font-family:"Montserrat",sans-serif;font-weight:700;font-size:40px;color:var(--dark)}
.side-label{position:absolute;left:70px;font-family:"Montserrat",sans-serif;font-weight:800;font-size:20px;letter-spacing:1px;color:#6b6b6b;transform:rotate(-90deg);transform-origin:left top;white-space:nowrap}
.spread{position:absolute;left:126px;width:666px;display:flex;box-shadow:0 2px 8px rgba(0,0,0,.25)}
.spread.outside{top:144px;height:442px}
.spread.inside{top:642px;height:444px}
.page{position:relative;width:333px;height:100%;background:var(--paper);overflow:hidden}
.abs{position:absolute}
.brand{font-family:"Montserrat",sans-serif;font-weight:600;color:var(--blue)}
.brand.white{color:#fff}
.photo{position:absolute}

/* outside left */
.gear-area{left:0;top:0;width:333px;height:216px;background:radial-gradient(circle at 30% 30%,#3a3d42,#15171a 70%)}
.benefits{left:106px;top:38px;list-style:none;font-size:9.5px;color:#fff;line-height:12px}
.benefits li::before{content:"• ";color:var(--blue-light)}
.pill{left:40px;top:128px;width:252px;height:20px;border:1.5px solid var(--blue-light);border-radius:10px;text-align:center;font-family:"Montserrat",sans-serif;font-weight:700;font-size:12.5px;line-height:17px;color:var(--blue-light);letter-spacing:.3px}
.qual-text{left:38px;top:154px;width:260px;text-align:center;font-size:9px;line-height:14px;color:#eee}
.blue-band{left:0;top:216px;width:333px;height:70px;background:linear-gradient(120deg,#3f86cf,#5aa1e4 60%,#4a94dc)}
.blue-band .brand{position:absolute;left:0;width:333px;top:22px;text-align:center;font-size:24px}
.worker-faded{left:0;top:286px;width:150px;height:132px;background:linear-gradient(90deg,#b8aea4,#e3e0dc)}
.contact{left:110px;top:312px;width:220px;text-align:center}
.contact h3{font-family:"Montserrat",sans-serif;font-weight:700;font-size:16px;color:var(--blue);letter-spacing:.5px}
.contact .icons{margin:6px 0 4px;display:flex;justify-content:center;gap:4px}
.contact p{font-size:9px;font-style:italic;line-height:12px;color:#222}
.footer{left:0;bottom:0;width:333px;height:24px;background:var(--dark);color:#fff;font-size:8px;line-height:24px}

/* outside right */
.mechanic-hood{width:333px;height:216px;background:linear-gradient(135deg,#7d8a99,#2d4f7c 55%,#1d2b44)}
.tagline-box{left:120px;top:216px;width:213px;height:70px;background:var(--dark);color:#fff;text-align:right;padding:8px 10px 0 0;font-family:"Montserrat",sans-serif;font-size:14px;line-height:19px}
.tagline-box b{font-weight:700}
.vehicles-label{left:22px;top:306px;font-family:"Open Sans",sans-serif;font-size:11px;line-height:15px;color:#333}
.truck{left:10px;top:340px;width:155px;height:72px;border-radius:6px;background:linear-gradient(180deg,#d8dde3,#9aa3ad)}
.phone-bar{right:0;bottom:0;width:158px;height:34px;background:var(--blue);color:#fff;font-family:"Montserrat",sans-serif;font-weight:700;font-size:16.5px;line-height:34px;text-align:center}

/* inside left */
.top-rule{left:0;top:0;width:100%;height:5px;background:var(--blue)}
.head{font-family:"Montserrat",sans-serif;font-weight:700;font-size:15.5px;line-height:18px;color:var(--ink)}
.head span{color:var(--blue);display:block}
.head::after{content:"";display:block;width:24px;height:2px;background:var(--dark);margin-top:6px}
.body-sm{font-size:6.6px;line-height:9px;color:var(--muted)}
.repair-photo{left:16px;top:128px;width:180px;height:125px;background:linear-gradient(135deg,#8c97a3,#34507a 60%,#1d2738)}
.mmc-box{left:206px;top:128px;width:110px;height:122px;background:var(--blue);color:#fff;font-family:"Oswald",sans-serif;font-weight:500;font-size:18px;line-height:26px;text-align:right;padding:22px 12px 0 0;white-space:nowrap}
.lead{left:16px;top:262px;width:228px;font-size:9.5px;line-height:11px;color:var(--ink);font-weight:600}
.lead em{font-style:normal;color:var(--blue)}
.subhead{font-family:"Montserrat",sans-serif;font-weight:700;font-size:11px;color:var(--blue)}
.pm-list{list-style:none;font-family:"Montserrat",sans-serif;font-weight:700;font-size:6px;line-height:9.2px;color:#333}
.pm-list li::before{content:"• "}
.tab{left:109px;top:360px;width:12px;height:48px;background:var(--blue);color:#1c2a40;font-size:5.5px;font-weight:700;writing-mode:vertical-rl;transform:rotate(180deg);text-align:center;line-height:12px}
.pm-intro{left:16px;top:360px;width:90px;font-size:6px;line-height:8px;color:var(--muted)}
.inside-footer{left:0;bottom:0;width:333px;height:26px;background:var(--dark);color:#fff;font-size:6.5px;line-height:8px;padding:5px 0 0 16px}

/* inside right */
.centered-head{left:0;top:28px;width:333px;text-align:center}
.centered-head .head::after{margin:6px auto 0}
.logo-box{left:16px;top:82px;width:110px;height:124px;background:var(--blue)}
.logo-box .brand{position:absolute;left:0;width:110px;top:52px;text-align:center;font-size:20px}
.clipboard-photo{left:126px;top:82px;width:186px;height:124px;background:linear-gradient(135deg,#8e9aa7,#3a5784 55%,#22324a)}
.service{width:142px;height:78px;border:1px solid #9cc3ea;text-align:center;padding-top:28px;background:var(--paper)}
.service h4{font-family:"Open Sans",sans-serif;font-weight:600;font-size:8.5px;color:#222;margin-bottom:4px}
.service p{font-size:5.2px;line-height:6.8px;color:#555;padding:0 6px}
.icon{width:38px;height:38px}
</style>
</head>
<body>
<div class="canvas">
  <div class="brand-top">RigCare</div>
  <div class="side-label" style="top:586px">BROCHURE OUTSIDE</div>
  <div class="side-label" style="top:1090px">BROCHURE INSIDE</div>

  <!-- OUTSIDE SPREAD -->
  <section class="spread outside">
    <article class="page back-cover">
      <div class="abs gear-area" role="img" aria-label="Dark machinery gears background"></div>
      <ul class="abs benefits">
        <li>Convenience</li>
        <li>Less employee time wasted</li>
        <li>Only one number to call</li>
        <li>Speed of repair</li>
        <li>Emergency roadside service</li>
        <li>Competitive Pricing</li>
        <li>All repairs – Major and Minor</li>
      </ul>
      <div class="abs pill">QUALIFIED SERVICE TECHNICIANS</div>
      <p class="abs qual-text">RigCare strives to have Service technicians with a minimum of 10 years experience and qualified in both diesel and gas engine maintenance.</p>
      <div class="abs blue-band"><div class="brand white">RigCare</div></div>
      <div class="photo worker-faded" role="img" aria-label="Faded photo of a mechanic holding a part"></div>
      <div class="abs contact">
        <h3>CONTACT US</h3>
        <div class="icons">
          <svg width="16" height="16" viewBox="0 0 16 16"><circle cx="8" cy="8" r="7" fill="none" stroke="#333"/><path d="M8 3.5a2.6 2.6 0 0 0-2.6 2.6C5.4 8.2 8 11.8 8 11.8s2.6-3.6 2.6-5.7A2.6 2.6 0 0 0 8 3.5z" fill="#333"/><circle cx="8" cy="6.1" r="1" fill="#fff"/></svg>
          <svg width="16" height="16" viewBox="0 0 16 16"><circle cx="8" cy="8" r="7" fill="none" stroke="#333"/><path d="M5.4 4.5l1.5-.3 1 2-1 .8a5 5 0 0 0 2.1 2.1l.8-1 2 1-.3 1.5c-3.4.3-6.4-2.7-6.1-6.1z" fill="#333"/></svg>
        </div>
        <p>4120 W 62nd Ave<br>Unit B Lakemont, CO 80099<br>303-555-0142</p>
      </div>
      <div class="abs footer" style="text-align:center;padding-left:90px">www.rigcarefleet.com</div>
    </article>

    <article class="page front-cover">
      <div class="photo mechanic-hood" style="left:0;top:0;clip-path:polygon(30px 0,333px 0,333px 216px,127px 216px)" role="img" aria-label="Photo of a mechanic in blue uniform working under a vehicle hood"></div>
      <svg class="abs" style="left:0;top:0" width="333" height="442" viewBox="0 0 333 442">
        <defs><linearGradient id="tri" x1="0" x2="1"><stop offset="0" stop-color="#3f86cf"/><stop offset="1" stop-color="#6cace4"/></linearGradient></defs>
        <polygon points="0,216 98,216 130,286 0,286" fill="url(#tri)"/>
        <polygon points="0,0 14,0 189,385 175,385" fill="#4a94dc"/>
        <polygon points="175,374 333,374 333,386 180,386" fill="#4a94dc"/>
        <polygon points="110,216 122,216 153,286 141,286" fill="#4a94dc"/>
      </svg>
      <div class="abs tagline-box">MOBILE<br>MECHANIC<br><b>COMPANY</b></div>
      <div class="abs vehicles-label">Specially Designed<br>Service Vehicles</div>
      <div class="photo truck" role="img" aria-label="White service utility truck"></div>
      <div class="abs brand" style="left:195px;top:338px;width:130px;text-align:center;font-size:26px">RigCare</div>
      <div class="abs footer" style="padding-left:15px">www.rigcarefleet.com</div>
      <div class="abs phone-bar">303-555-0187</div>
    </article>
  </section>

  <!-- INSIDE SPREAD -->
  <section class="spread inside">
    <article class="page inside-left">
      <div class="abs top-rule"></div>
      <h2 class="abs head" style="left:16px;top:28px">SPECIALLY DESIGNED<span>SERVICE VEHICLES</span></h2>
      <div class="abs brand" style="left:222px;top:44px;font-size:19px">RigCare</div>
      <p class="abs body-sm" style="left:16px;top:76px;width:300px">Our service vehicles are specially designed and equipped to perform up to 85% of all vehicle maintenance and repair requirements on-site.</p>
      <p class="abs body-sm" style="left:16px;top:100px;width:300px">Waste oil is pumped into onboard holding tanks and disposed through certified oil recycling companies. This keeps the work area neat and clean without an oil mess.</p>
      <div class="photo repair-photo" role="img" aria-label="Photo of a mechanic repairing an engine"></div>
      <svg class="abs" style="left:0;top:0" width="333" height="444" viewBox="0 0 333 444">
        <polygon points="186,128 200,128 333,425 333,444 318,444" fill="#4a94dc"/>
        <polygon points="248,256 262,256 333,420 333,444 324,444" fill="#2a2c30"/>
        <polygon points="268,256 282,256 333,374 333,404" fill="#2a2c30"/>
      </svg>
      <div class="abs mmc-box">MOBILE<br>MECHANIC<br>COMPANY</div>
      <p class="abs lead">You don't bring your fleet vehicles to us, <em>we come to you on a routine or emergency basis.</em></p>
      <p class="abs body-sm" style="left:16px;top:289px;width:240px">We service your cars, trucks and trailers at your location and convenience.</p>
      <p class="abs body-sm" style="left:16px;top:300px;width:228px">Our on-site service enables you to fully utilize your fleet and personnel, saving time and expense by providing service and convenience.</p>
      <p class="abs body-sm" style="left:16px;top:321px;width:228px">Your personnel can perform their job and your vehicles can stay on schedule, minimizing down time for servicing.</p>
      <h3 class="abs subhead" style="left:16px;top:342px">PREVENTIVE MAINTENANCE INSPECTION</h3>
      <p class="abs pm-intro">Our preventive maintenance checklist program offers a systematic and thorough approach to vehicle maintenance and repair.</p>
      <div class="abs tab">OUR INSPECTION</div>
      <ul class="abs pm-list" style="left:132px;top:359px"><li>BRAKES</li><li>SUSPENSION</li><li>EXHAUST</li><li>HOSES</li><li>PUMPS</li><li>FLUIDS</li></ul>
      <ul class="abs pm-list" style="left:190px;top:359px"><li>ELECTRICAL SYSTEM</li><li>DRIVE TRAIN</li><li>BELTS</li><li>PULLEYS</li><li>COOLING SYSTEM</li></ul>
      <div class="abs inside-footer">This program also provides the fleet manager with PM frequency recommendations and detailed report<br>of the repair service performed.</div>
    </article>

    <article class="page inside-right">
      <div class="abs top-rule"></div>
      <div class="abs centered-head"><h2 class="head">FLEET MANAGER<span>WITHOUT THE COST</span></h2></div>
      <div class="abs logo-box"><div class="brand white">RigCare</div></div>
      <div class="photo clipboard-photo" role="img" aria-label="Photo of a mechanic with a clipboard inspecting an engine"></div>

      <div class="abs service" style="left:16px;top:236px">
        <h4>Preventive Schedule</h4>
        <p>We track the service needs of every vehicle in your fleet and let you know when each one is due for care.</p>
      </div>
      <div class="abs service" style="left:170px;top:236px">
        <h4>Major or Minor Repairs</h4>
        <p>We handle the small fixes and the big jobs alike. No need to wait on drivers to report when vehicles are ready.</p>
      </div>
      <div class="abs service" style="left:16px;top:326px">
        <h4>Overflow Service</h4>
        <p>Already have a fleet manager or in-house mechanics? No problem. We can take on overflow work to catch your team up.</p>
      </div>
      <div class="abs service" style="left:170px;top:326px">
        <h4>Keep Vehicles on the Road</h4>
        <p>In most cases we repair your vehicle on site and get it back to work fast, avoiding towing fees and long down time.</p>
      </div>

      <svg class="abs icon" style="left:68px;top:216px" viewBox="0 0 38 38"><circle cx="19" cy="19" r="19" fill="#4a94dc"/><rect x="12" y="10" width="14" height="18" rx="1.5" fill="none" stroke="#fff" stroke-width="1.6"/><rect x="16" y="8" width="6" height="4" fill="#fff"/><path d="M14.5 16l1.2 1.2 2-2M14.5 21l1.2 1.2 2-2M20 16h4M20 21h4" stroke="#fff" stroke-width="1.3" fill="none"/></svg>
      <svg class="abs icon" style="left:222px;top:216px" viewBox="0 0 38 38"><circle cx="19" cy="19" r="19" fill="#4a94dc"/><path d="M11 27l10-10M17 11l10 10" stroke="#fff" stroke-width="2.6" stroke-linecap="round"/><circle cx="24" cy="14" r="3" fill="none" stroke="#fff" stroke-width="1.8"/></svg>
      <svg class="abs icon" style="left:68px;top:306px" viewBox="0 0 38 38"><circle cx="19" cy="19" r="19" fill="#4a94dc"/><circle cx="19" cy="15" r="5" fill="none" stroke="#fff" stroke-width="2.4" stroke-dasharray="2.5 1.5"/><circle cx="19" cy="15" r="1.8" fill="#fff"/><path d="M9 26c4-3 7-2 10-1s5 0 9-3" stroke="#fff" stroke-width="2" fill="none" stroke-linecap="round"/></svg>
      <svg class="abs icon" style="left:222px;top:306px" viewBox="0 0 38 38"><circle cx="19" cy="19" r="19" fill="#4a94dc"/><path d="M12 20l2-6h10l2 6v6h-14z" fill="none" stroke="#fff" stroke-width="1.8"/><circle cx="15" cy="22" r="1.3" fill="#fff"/><circle cx="23" cy="22" r="1.3" fill="#fff"/></svg>

      <div class="abs footer" style="height:26px;line-height:26px;padding-left:16px">www.rigcarefleet.com</div>
      <div class="abs phone-bar" style="height:34px">303-555-0187</div>
    </article>
  </section>
</div>
</body>
</html>
```